Business Card Design Project

I am looking for a classy business card design for a product design consultancy. We specialize in Product Design, Prototyping, and Manufacturing Consulting. Products that we design range from consumer electronics to household products all the way to sporting goods. We are based in Arizona and called "Heron Design Works." We like to have fun and goof off as much as we like to create new products. We are young and energetic so we would like our business cards to reflect that. We already have a logo that we would like to implement into the card design. A plain rectangular business card is boring so feel free to get creative, but please, no avocado shaped cards (it's far too literal). Also feel free to play around with textured card stocks or plastic. The final design that we choose will pay attention to all of the little details. Our cards will need to be 2 sided. We're giving you guys free reign to design as you would like. Please have fun with this, it will reflect in our business card.

Thanks guys,
Heron Design Works Team

Industry/Entity Type

Electronics

Requirements
Must have
• We would like to have a spot UV coating somewhere on the business card design if possible.
Nice to have
• Let's see some designs with custom shapes rather than typical rectangular business cards but please no avocado shaped cards, thanks. Also play around with textured card socks.

```html
<!DOCTYPE html>
<html lang="en">
<head>
<meta charset="utf-8">
<title>Heron Design Works – Business Card</title>
<link rel="stylesheet" href="https://fonts.googleapis.com/css2?family=Questrial&family=Open+Sans:wght@300;400;700&display=swap">
<style>
  :root {
    --backdrop: #e9e6e1;
    --card-green: #8fd43a;
    --oval-green: #a6e54f;
    --spot-uv: #93d845;
    --card-white: #f4f4f2;
    --brand-green: #7cc42c;
    --ink-grey: #8a8a8a;
    --ink-dark: #9a9a9a;
  }
  html, body {
    margin: 0;
    width: 1200px;
    height: 1000px;
    overflow: hidden;
    background: var(--backdrop);
  }
  .canvas { display: block; width: 1200px; height: 1000px; }
  .card-front-shape { fill: var(--card-green); }
  .uv-oval { fill: var(--oval-green); }
  .uv-wordmark {
    font-family: "Questrial", sans-serif;
    font-size: 27px;
    fill: var(--spot-uv);
    text-anchor: middle;
  }
  .card-back-shape { fill: var(--card-white); }
  .person-name {
    font-family: "Questrial", sans-serif;
    font-size: 42px;
    fill: var(--brand-green);
    text-anchor: middle;
  }
  .person-title {
    font-family: "Open Sans", sans-serif;
    font-weight: 400;
    font-size: 17px;
    letter-spacing: 2px;
    fill: var(--ink-grey);
    text-anchor: middle;
  }
  .contact-line {
    font-family: "Open Sans", sans-serif;
    font-weight: 300;
    font-size: 19px;
    fill: var(--ink-grey);
    text-anchor: middle;
  }
  .brand-name {
    font-family: "Questrial", sans-serif;
    font-size: 27px;
    fill: var(--brand-green);
    text-anchor: start;
  }
  .brand-dot { fill: var(--brand-green); }
  .web-address {
    font-family: "Open Sans", sans-serif;
    font-weight: 300;
    font-size: 21px;
    fill: var(--ink-dark);
    text-anchor: middle;
  }
  .web-address .strong { font-weight: 700; }
</style>
</head>
<body>
<svg class="canvas" viewBox="0 0 1200 1000" xmlns="http://www.w3.org/2000/svg">
  <defs>
    <!-- Custom die-cut: rectangle with two large sweeping corners -->
    <path id="card-outline" d="M60 0 H278 A200 200 0 0 1 478 200 V647 A60 60 0 0 1 418 707 H200 A200 200 0 0 1 0 507 V60 A60 60 0 0 1 60 0 Z"/>
  </defs>

  <!-- Front side: green card with spot UV oval -->
  <g class="card-front" transform="translate(97 140) scale(1.07 1.08)">
    <use href="#card-outline" class="card-front-shape"/>
  </g>
  <g class="uv-area">
    <ellipse class="uv-oval" cx="333" cy="680" rx="146" ry="158"/>
    <text class="uv-wordmark" x="333" y="700">Heron Design Works</text>
  </g>

  <!-- Back side: white card with contact details -->
  <g class="card-back" transform="translate(637 50)">
    <use href="#card-outline" class="card-back-shape"/>
  </g>
  <g class="card-back-text">
    <text class="person-name" x="880" y="328">milo harper</text>
    <text class="person-title" x="880" y="361">PRESIDENT</text>
    <text class="contact-line" x="880" y="411">o | 480.555.0147</text>
    <text class="contact-line" x="880" y="438">c | 602.555.0182</text>
    <text class="contact-line" x="880" y="466">milo@herondesignworks.com</text>
    <circle class="brand-dot" cx="760" cy="571" r="8"/>
    <text class="brand-name" x="778" y="580">Heron Design Works</text>
    <text class="web-address" x="880" y="630"><tspan class="strong">heron</tspan>designworks<tspan class="strong">.com</tspan></text>
  </g>
</svg>
</body>
</html>
```